QuillMark Business Cards

I need a business card designed for QuillMark. To get an idea of what we do please visit https://formvault.example/para-creadores-3

```html
<!DOCTYPE html>
<html lang="en">
<head>
<meta charset="utf-8">
<title>QuillMark Business Cards</title>
<link rel="stylesheet" href="https://fonts.googleapis.com/css2?family=Montserrat:wght@300;400&display=swap">
<style>
  :root {
    --page: #ffffff;
    --card: #1b1f22;
    --gold: #e8961f;
    --ink: #ffffff;
    --rule: #cfd2d4;
  }
  html, body {
    margin: 0;
    width: 1200px;
    height: 1200px;
    overflow: hidden;
    background: var(--page);
    font-family: "Montserrat", sans-serif;
  }
  .canvas {
    position: relative;
    width: 1200px;
    height: 1200px;
  }
  .card {
    position: absolute;
    width: 872px;
    height: 522px;
    background: var(--card);
  }
  .card--front { left: 171px; top: 44px; }
  .card--back {
    left: 169px;
    top: 588px;
    box-shadow: 2px 4px 8px rgba(0, 0, 0, 0.22);
  }
  .front-name {
    position: absolute;
    left: 0;
    right: 0;
    top: 50%;
    margin: 0;
    transform: translateY(-50%);
    text-align: center;
    color: var(--gold);
    font-weight: 300;
    font-size: 40px;
    letter-spacing: 0.32em;
    padding-left: 0.32em;
  }
  .brand {
    position: absolute;
    left: 161px;
    top: 96px;
  }
  .brand-name {
    color: var(--ink);
    font-weight: 300;
    font-size: 27px;
    letter-spacing: 0.3em;
    line-height: 1;
    margin: 0;
  }
  .brand-tagline {
    display: flex;
    align-items: center;
    margin-top: 12px;
    color: var(--gold);
    font-size: 7.5px;
    letter-spacing: 0.62em;
    text-transform: uppercase;
  }
  .brand-tagline::after {
    content: "";
    display: block;
    width: 92px;
    height: 1px;
    background: var(--rule);
  }
  .contact {
    position: absolute;
    left: 372px;
    top: 226px;
    margin: 0;
    padding: 0;
    list-style: none;
  }
  .contact-item {
    display: flex;
    align-items: center;
    height: 37px;
    color: var(--ink);
    font-weight: 300;
    font-size: 27px;
    letter-spacing: -0.01em;
    white-space: nowrap;
  }
  .contact-item:nth-child(3) { margin-top: 4px; }
  .contact-icon {
    width: 32px;
    height: 28px;
    margin-right: 14px;
    flex: none;
    fill: none;
    stroke: var(--gold);
    stroke-width: 1.8;
    stroke-linecap: round;
    stroke-linejoin: round;
  }
</style>
</head>
<body>
<main class="canvas">
  <section class="card card--front">
    <p class="front-name">QUILLMARK</p>
  </section>

  <section class="card card--back">
    <div class="brand">
      <h1 class="brand-name">QUILLMARK</h1>
      <div class="brand-tagline">Digital Notary</div>
    </div>

    <ul class="contact">
      <li class="contact-item">
        <svg class="contact-icon" viewBox="0 0 32 28" aria-hidden="true">
          <rect x="2" y="3" width="28" height="22" rx="3"/>
          <path d="M6 7 L16 17 L26 7"/>
        </svg>
        hello@quillmail.example
      </li>
      <li class="contact-item">
        <svg class="contact-icon" viewBox="0 0 32 28" aria-hidden="true">
          <path d="M7 2 L7 24 L12 18 L15 25 L17 24 L14 17 L22 16 Z"/>
        </svg>
        www.quillmark.example
      </li>
      <li class="contact-item">
        <svg class="contact-icon" viewBox="0 0 32 28" aria-hidden="true">
          <path d="M16 26 C10 19 6 15 6 10 A10 10 0 0 1 26 10 C26 15 22 19 16 26 Z"/>
          <circle cx="16" cy="10" r="3.5"/>
        </svg>
        524-1190 Harbor St.
      </li>
      <li class="contact-item">
        <svg class="contact-icon" viewBox="0 0 32 28" aria-hidden="true">
          <path d="M16 2 C10 4 8 10 9 16 C10 22 13 26 17 26 C18 25 18 23 17 22 C15 22 14 20 13 17 C12 13 13 9 15 7 C17 6 17 3 16 2 Z"/>
        </svg>
        90482736615-40
      </li>
    </ul>
  </section>
</main>
</body>
</html>
```